We are looking to improve our packaging, because we are wanting to secure our products into five star hotels, spa and wellness centres and maybe even high end retail department stores. That is why it is important it must look the part. We are even prepared to change our current packaging (White stand up pouches) for something different e.g box etc...

Please keep in mind when designing our new Serenwell packaging that our product range will extend to Room Sprays, Candles, Diffuser, Essential Oils, Soaps, Body Scrubs, Milk Baths, Body Lotions, Face Products. So the design will need to compliment and we must be able to adjust the artwork with ease to fit bottles big and small, tubes, boxes glass jars etc... at later stage.

Please see inspiration images of packaging I like. But please do not copy them. We would like something that is unique to our brand that will last for 2-4 years before we have to change the packaging again.

Our current packaging is in a white stand up pouches.
Updates

Project Deadline Extended Reason: Hi All,I have decided to extend the Serenwell Calm Mix Packaging project as the designs I have received are not what I am looking for and are not polished enough for the retail health and spa market. Some of the ideas I received are on the right track, but they need to be reworked a bit more to give our packaging a premium high end looking product. I am trying to get our products into large retail outlets department stores, Chemists, Health and natural product stores, 5 star spa resorts and hotels and eventually export it globally and with so many similar products available for sale our products needs to stand out from the rest of the competition. We use premium grade salts with natural and organic ingredients in our products when we make them. They do not have any harsh chemicals in them. At the moment I am keeping to the stand up white pouches for now, but this will change later this year to a box. We have a good product that sells well, but our current look and feel of our packaging is letting us down and making it difficult to market into the bigger retail stores. I have attached a few sample ideas of what we like, but with our own unique mark to it. We would like something that is unique to us to give our Serenwell brand its own identity. I will leave this up to your creative skills.Our Serenwell product range will branch out to the following in a couple of months. Body Scrubs, Liquid Soaps, Soaps, Body and Face Lotions, Milk baths, Bath and Spa Tea Bags, Bubble Paths, Herbal and Fragranced Bath & Spa products, Steam Therapy, Massage and Bath Oils, Room Sprays, Home Fragrances and Essential oils. So please keep this mind when designing a label that it must be easily adapted to different shapes and size products. e.g. boxes, jars, tubes and bottles.If you have any question before you start, please send me a message.Thank you for taking the time to read our extended brief and very excited to see your designs. Kind Regards, Added Saturday, January 9, 2016

Target Market(s)

Male and female, natural products, well-being, holistic, wellness centres, spa resorts, 5 stars hotels and upmarket.

Industry/Entity Type

Health And Wellness

Font styles to use
Serif
Sans Serif
Other font styles liked:
• Open Sans

Requirements
Must have
• Front: Company Name: Brand name Serenwell Calm Mix (See logo attached or feel fry to add your design flair to this). Please insert Front Packaging copy, 100% pure & natural logo, weight of item 1kg
• Back: Palvex logo (attached), Australian Packed & Owned logo (attached or you can just use type), Please use Back Packaging copy attached. Please allow space for barcode, Batch number and expiry date.
Nice to have
• Vector background, natural earthy feel, natural or organic textures
• but we are open to any suggestions you might have.

```html
<!DOCTYPE html>
<html lang="en">
<head>
<meta charset="utf-8">
<title>Serenwell Calm Mix – Bath Salt Label</title>
<link rel="stylesheet" href="https://fonts.googleapis.com/css2?family=Great+Vibes&family=Playfair+Display:wght@700;800&family=Fira+Sans+Condensed:wght@600&family=Questrial&family=Open+Sans:wght@700&display=swap">
<style>
  :root {
    --magenta: #e6157f;
    --violet: #7b2fa6;
    --purple: #5b2a8f;
    --ink: #1c1c1c;
    --paper: #ffffff;
    --floral-light: #c98be0;
    --floral-deep: #8a3cb8;
  }
  * { margin: 0; padding: 0; box-sizing: border-box; }
  html, body {
    width: 847px; height: 1200px; overflow: hidden; background: var(--paper);
  }
  .label {
    position: relative; width: 847px; height: 1200px;
    background: var(--paper); overflow: hidden;
  }
  .band { position: absolute; left: 0; width: 847px; display: block; }
  .band--top { top: 0; height: 70px; }
  .band--bottom { bottom: 0; height: 90px; }

  .floral-art {
    position: absolute; left: 520px; top: 540px; width: 310px; height: 600px;
    border-radius: 50% 40% 30% 45% / 30% 35% 20% 25%;
    background: radial-gradient(ellipse at 55% 40%, var(--floral-light) 0%, rgba(201,139,224,0.55) 45%, rgba(255,255,255,0) 75%),
                linear-gradient(170deg, rgba(138,60,184,0.35), rgba(230,21,127,0.25));
    opacity: 0.85;
  }

  .origin-script {
    position: absolute; left: 78px; top: 58px;
    font-family: "Great Vibes", cursive;
    color: var(--violet); font-size: 124px; line-height: 118px;
  }
  .quality-seal {
    position: absolute; left: 560px; top: 93px; width: 226px; height: 226px;
    border-radius: 50%;
    background: var(--magenta);
    box-shadow: inset 0 0 0 14px var(--paper), inset 0 0 0 22px var(--violet);
  }

  .product-name {
    position: absolute; left: 80px; top: 398px;
    font-family: "Playfair Display", serif; font-weight: 800;
    color: var(--magenta); font-size: 104px; line-height: 116px;
    letter-spacing: 1px; text-transform: uppercase;
  }
  .product-type {
    position: absolute; left: 82px; top: 762px;
    font-family: "Fira Sans Condensed", sans-serif; font-weight: 600;
    color: var(--purple); font-size: 60px; line-height: 70px;
  }
  .ingredients {
    position: absolute; left: 82px; top: 850px;
    font-family: "Questrial", sans-serif;
    color: var(--ink); font-size: 47px; line-height: 55px;
  }
  .net-weight {
    position: absolute; right: 22px; bottom: 26px;
    font-family: "Open Sans", sans-serif; font-weight: 700;
    color: var(--paper); font-size: 38px; line-height: 40px;
  }
</style>
</head>
<body>
<main class="label">
  <svg class="band band--top" viewBox="0 0 847 70" preserveAspectRatio="none" aria-hidden="true">
    <defs>
      <linearGradient id="bandTop" x1="0" y1="0" x2="1" y2="0">
        <stop offset="0" stop-color="#e6157f"/>
        <stop offset="1" stop-color="#7b2fa6"/>
      </linearGradient>
    </defs>
    <path d="M0 0 H847 V58 C640 20 300 10 0 36 Z" fill="url(#bandTop)"/>
  </svg>

  <div class="floral-art" role="img" aria-label="Decorative flowering vine illustration with butterflies in purple and magenta"></div>

  <div class="origin-script">Australian<br>Packed</div>
  <div class="quality-seal" role="img" aria-label="Quality seal"></div>

  <h1 class="product-name">Serenwell<br>Calm<br>Mix</h1>
  <p class="product-type">Bath Salt</p>
  <p class="ingredients">Himalayan Salt,<br>Magnesium<br>Chloride Flakes<br>and Vitamin C</p>

  <svg class="band band--bottom" viewBox="0 0 847 90" preserveAspectRatio="none" aria-hidden="true">
    <defs>
      <linearGradient id="bandBottom" x1="0" y1="0" x2="1" y2="0">
        <stop offset="0" stop-color="#e6157f"/>
        <stop offset="1" stop-color="#7b2fa6"/>
      </linearGradient>
    </defs>
    <path d="M0 58 C280 30 600 20 847 10 V90 H0 Z" fill="url(#bandBottom)"/>
  </svg>
  <p class="net-weight">1kg</p>
</main>
</body>
</html>
```